CT Bellmere 2018-2019 Season Poster

Poster for the Orchestra's 208-2019 concert season

Text for the Poster:
___________________
Connecticut Bellmere Chamber Orchestra
Teodor Vashkin - founder and artistic director
Since 1997 | Preserving the chamber orchestral musical traditions through public performances, education, and by showcasing regional & international artists

2018-2019 Season

Harold Pensby: Nocturne of Quarries
Soloist: Mirela Oskarsdottir-Fenwick, piano
Anton Varkell: Kevätsade (The Spring Rain)
Program bridging heritage of Europe, Israel, and North America.

Fri. October 12 / 8 pm / New Britain
Elmhurst Hill Congregational (417 Tolland Ave)
Sat. October 13 / 8 pm / Hartford
Anselm and Bruno Church, Hartford (92 Quillby Ave)
-----------------

Lisette by L. Marotte
Marotte’s immortal opera, Lisette, fully staged with English super-title
translations.

Fri. November 9 / 7:30 pm / New Britain
Halden-On-Rise (214 Ferncroft St)
Sun. November 11 / 4 pm / New London
Pruitt Arts Center (718 Harlow St)
Sat. November 17 / 7:30 / Middletown
KRW Performing Arts Center (415 Bexley Ln)
Sun. November 18 / 2 pm / Hartford
Pemberly Lyceum Museum of Art (381 Wrenfield St)
-----------------

Annual Polish Christmas Concert
The Bellmere will be joined by Zawadzki Choir in a program containing some Christmas favorites.

Sun. December 9 / Time TBA / Hartford
Cathedral of Saint Ambrose (276 Ashgrove Ave)
December 16 / 4 pm / New Britain
-----------------

Die Gräfin von Morland by K. Dravec
Fully staged opera in partnership with Connecticut Fernway Opera. In
commemoration of Annual Lantern Vigil Day.

January/February 2019 – DATES and TIMES TBA
-------------------

Jazz Cross-Over with Lucy Pell
The Connecticut Bellmere will perform music from the popular film series, and some jazz standards.

Fri. March 22 / 8 pm / New Britain
Sun. March 24 / 4 pm / Hartford
---------------------

Ottavio Lanfredi: Velmira
Lanfredi’s swansong has a claim to being the last great popular opera,
fully staged production.

Fri. May 10 / 7:30 pm / New Britain
Sat. May 11 / 7:30 pm / Middletown
Fri. May 17 / 7:30 pm / New London
Pruitt Arts Center (718 Harlow St.)
Sun. May 26 / 2 pm / Hartford
------------------------

Songs of the Turning Tides
Hollweck: Symphony No. 3 (Pastorella)
Pelyavin String Symphony No. 8
Concert program exploring music that reflected milestone events of
social change.

Fri. May 31 / 8 pm / New Britain
Sun. June 2 / 2 pm / Hartford

CONTACT:

860 555-0147
www.thebellmere-ens.org
info@thebellmere-ens.org

Target Market(s)

Arts community

Industry/Entity Type

Performing Art

Font styles to use
Serif
Sans Serif
Other font styles liked:
• Calibri

Colors

Designer to choose colors to be used in the design.

Requirements
Must have
• creative concept
Nice to have
• modern, almost avant-garde - but with clear concept of music

```html
<!DOCTYPE html>
<html lang="en">
<head>
<meta charset="utf-8">
<title>Connecticut Bellmere Chamber Orchestra – 2018-2019 Season</title>
<link rel="stylesheet" href="https://fonts.googleapis.com/css2?family=Tenor+Sans&family=Alegreya+SC:wght@700&family=Alegreya+Sans:wght@400;700&family=Pinyon+Script&display=swap">
<style>
  :root {
    --crimson: #bb1a30;
    --ink: #231f20;
    --paper: #ffffff;
    --frame: #9a9a9a;
    --hall-light: #c98a63;
    --hall-dark: #2a1712;
  }
  * { box-sizing: border-box; margin: 0; padding: 0; }
  html, body { width: 783px; height: 1200px; overflow: hidden; background: var(--paper); }
  .poster {
    position: relative; width: 783px; height: 1200px; overflow: hidden;
    background: var(--paper); color: var(--ink);
    font-family: "Alegreya Sans", "Calibri", sans-serif;
  }
  .frame { position: absolute; left: 8px; top: 360px; width: 768px; height: 832px; border: 1px solid var(--frame); border-top: none; }
  .hero {
    position: absolute; left: 0; top: 0; width: 783px; height: 369px;
    background: linear-gradient(180deg, #7a4a36 0%, var(--hall-light) 30%, #a8664a 58%, var(--hall-dark) 100%);
  }
  .hero-text { position: absolute; left: 0; top: 0; width: 783px; color: var(--paper); }
  .title {
    position: absolute; top: 68px; width: 100%; text-align: center;
    font-family: "Tenor Sans", sans-serif; font-variant: small-caps; font-size: 48px; line-height: 1; letter-spacing: 0.5px;
  }
  .subtitle {
    position: absolute; top: 130px; left: 0; width: 783px; text-align: center; padding-left: 10px;
    font-family: "Tenor Sans", sans-serif; font-variant: small-caps; font-size: 26px; line-height: 1;
  }
  .director { position: absolute; left: 225px; top: 161px; font-family: "Tenor Sans", sans-serif; font-variant: small-caps; font-size: 16px; }
  .mission { position: absolute; left: 225px; top: 180px; width: 300px; font-size: 11.5px; line-height: 1.3; }
  .season {
    position: absolute; left: 0; top: 296px; width: 783px; text-align: center; padding-left: 20px;
    font-family: "Pinyon Script", cursive; font-size: 62px; line-height: 1; color: var(--paper);
    text-shadow: 0 2px 4px rgba(0,0,0,0.5);
  }
  .band { position: absolute; left: 0; width: 783px; background: var(--crimson); }
  .band-top { top: 369px; height: 112px; }
  .band-mid { top: 777px; left: 3px; width: 776px; height: 124px; }
  .photo { position: absolute; border: 1px solid #d9d9d9; }
  .photo-soloist { left: 33px; top: 374px; width: 149px; height: 182px; background: linear-gradient(160deg, #3a3431, #6b4a3c 55%, #1f1b1a); }
  .photo-lisette { left: 216px; top: 383px; width: 118px; height: 173px; background: linear-gradient(180deg, #8a7d6c, #5a3e30 40%, #3d63b5 75%, #2e4f98); }
  .photo-singer { left: 402px; top: 413px; width: 158px; height: 143px; background: linear-gradient(150deg, #4d3326, #b77c55 50%, #2e1d16); }
  .photo-staging { left: 583px; top: 379px; width: 157px; height: 177px; background: linear-gradient(170deg, #5d5754, #c9c3bd 45%, #7a8392 80%, #3a3633); }
  .photo-choir { left: 214px; top: 822px; width: 162px; height: 92px; background: linear-gradient(180deg, #8e8680, #3c3434 55%, #201c1c); }
  .photo-velmira { left: 396px; top: 820px; width: 168px; height: 94px; background: linear-gradient(160deg, #e7c16a, #d08a3c 50%, #8f3b1f); }
  .photo-composer { left: 580px; top: 754px; width: 161px; height: 160px; background: linear-gradient(160deg, #6b4a2e, #b9a089 45%, #2b1d14 75%, #a3271f); }
  .event { position: absolute; font-size: 11.5px; line-height: 1.27; }
  .event h2 { font-family: "Alegreya SC", serif; font-weight: 700; font-size: 13.5px; line-height: 1.22; margin-bottom: 1px; }
  .event .dates { margin-top: 9px; }
  .event .date { font-size: 9.5px; line-height: 1.3; margin-bottom: 6px; }
  .event .date b { font-weight: 700; }
  .ev-pensby { left: 33px; top: 564px; width: 170px; }
  .ev-lisette { left: 216px; top: 564px; width: 178px; }
  .ev-jazz { left: 402px; top: 564px; width: 168px; }
  .ev-grafin { left: 583px; top: 564px; width: 175px; }
  .ev-polish { left: 218px; top: 923px; width: 165px; }
  .ev-velmira { left: 396px; top: 923px; width: 172px; }
  .ev-tides { left: 580px; top: 923px; width: 170px; }
  .contact { position: absolute; left: 38px; top: 795px; color: var(--paper); font-weight: 700; font-size: 15.5px; line-height: 1.38; }
  .sponsors { position: absolute; left: 41px; top: 910px; font-size: 12.5px; }
</style>
</head>
<body>
<main class="poster">
  <div class="hero" role="img" aria-label="Chamber orchestra performing on a wood-panelled concert stage with a conductor"></div>
  <header class="hero-text">
    <h1 class="title">Connecticut Bellmere</h1>
    <p class="subtitle">Chamber Orchestra</p>
    <p class="director">Teodor Vashkin - founder and artistic director</p>
    <p class="mission">Since 1997 | Preserving the chamber orchestral musical traditions through public performances, education, and by showcasing regional &amp; international artists</p>
  </header>
  <div class="frame"></div>
  <div class="band band-top"></div>
  <p class="season">2018-2019 Season</p>
  <div class="band band-mid"></div>

  <div class="photo photo-soloist" role="img" aria-label="Portrait of the piano soloist"></div>
  <div class="photo photo-lisette" role="img" aria-label="Portrait of a soprano in a blue dress"></div>
  <div class="photo photo-singer" role="img" aria-label="Portrait of the jazz singer"></div>
  <div class="photo photo-staging" role="img" aria-label="Scene from a staged opera production"></div>
  <div class="photo photo-choir" role="img" aria-label="Choir group photo in dark robes"></div>
  <div class="photo photo-velmira" role="img" aria-label="Vintage opera poster illustration"></div>
  <div class="photo photo-composer" role="img" aria-label="Painted portrait of the composer"></div>

  <section class="event ev-pensby">
    <h2>Harold Pensby: Nocturne of Quarries</h2>
    <p>Soloist: Mirela Oskarsdottir-Fenwick, piano</p>
    <p>Anton Varkell: Kevätsade (The Spring Rain)</p>
    <p>Program bridging heritage of Europe, Israel, and North America.</p>
    <div class="dates">
      <p class="date"><b>Fri. October 12</b> / 8 pm / New Britain<br>Elmhurst Hill Congregational<br>(417 Tolland Ave)</p>
      <p class="date"><b>Sat. October 13</b> / 8 pm / Hartford<br>Anselm and Bruno Church, Hartford<br>(92 Quillby Ave)</p>
    </div>
  </section>

  <section class="event ev-lisette">
    <h2>Lisette by L. Marotte</h2>
    <p>Marotte’s immortal opera, Lisette, fully staged with English super-title translations.</p>
    <div class="dates">
      <p class="date"><b>Fri. November 9</b> / 7:30 pm / New Britain<br>Halden-On-Rise (214 Ferncroft St)</p>
      <p class="date"><b>Sun. November 11</b> / 4 pm / New London<br>Pruitt Arts Center (718 Harlow St)</p>
      <p class="date"><b>Sat. November 17</b> / 7:30 / Middletown<br>KRW Performing Arts Center<br>(415 Bexley Ln)</p>
      <p class="date"><b>Sun. November 18</b> / 2 pm / Hartford<br>Pemberly Lyceum Museum of Art<br>(381 Wrenfield St)</p>
    </div>
  </section>

  <section class="event ev-jazz">
    <h2>Jazz Cross-Over with Lucy Pell</h2>
    <p>The Connecticut Bellmere will perform music from the popular film series, and some jazz standards.</p>
    <div class="dates">
      <p class="date"><b>Fri. March 22</b> / 8 pm / New Britain<br>Elmhurst Hill Congregational<br>(417 Tolland Ave)</p>
      <p class="date"><b>Sun. March 24</b> / 4 pm / Hartford<br>Anselm and Bruno Church, Hartford<br>(92 Quillby Ave)</p>
    </div>
  </section>

  <section class="event ev-grafin">
    <h2>Die Gräfin von Morland by K. Dravec</h2>
    <p>Fully staged opera in partnership with Connecticut Fernway Opera. In commemoration of Annual Lantern Vigil Day.</p>
    <div class="dates">
      <p class="date"><b>January/February 2019</b> – DATES and TIMES TBA</p>
    </div>
  </section>

  <div class="contact">
    <p>CONTACT:</p>
    <p>860 555-0147</p>
    <p>www.thebellmere-ens.org</p>
    <p>info@thebellmere-ens.org</p>
  </div>
  <p class="sponsors">Sponsors</p>

  <section class="event ev-polish">
    <h2>Annual Polish Christmas Concert</h2>
    <p>The Bellmere will be joined by Zawadzki Choir in a program containing some Christmas favorites.</p>
    <div class="dates">
      <p class="date"><b>Sun. December 9</b> / Time TBA / Hartford<br>Cathedral of Saint Ambrose<br>(276 Ashgrove Ave)</p>
      <p class="date"><b>December 16</b> / 4 pm / New Britain<br>Halden-On-Rise (214 Ferncroft St)</p>
    </div>
  </section>

  <section class="event ev-velmira">
    <h2>Ottavio Lanfredi: Velmira</h2>
    <p>Lanfredi’s swansong has a claim to being the last great popular opera, fully staged production.</p>
    <div class="dates">
      <p class="date"><b>Fri. May 10</b> / 7:30 pm / New Britain<br>Halden-On-Rise (214 Ferncroft St)</p>
      <p class="date"><b>Sat. May 11</b> / 7:30 pm / Middletown<br>KRW Performing Arts Center<br>(415 Bexley Ln)</p>
      <p class="date"><b>Fri. May 17</b> / 7:30 pm / New London<br>Pruitt Arts Center (718 Harlow St.)</p>
      <p class="date"><b>Sun. May 26</b> / 2 pm / Hartford<br>Pemberly Lyceum Museum of Art<br>(381 Wrenfield St)</p>
    </div>
  </section>

  <section class="event ev-tides">
    <h2>Songs of the Turning Tides</h2>
    <p>Hollweck: Symphony No. 3 (Pastorella)<br>Pelyavin String Symphony No. 8<br>Concert program exploring music that reflected milestone events of social change.</p>
    <div class="dates">
      <p class="date"><b>Fri. May 31</b> / 8 pm / New Britain<br>Elmhurst Hill Congregational<br>(417 Tolland Ave)</p>
      <p class="date"><b>Sun. June 2</b> / 2 pm / Hartford<br>Pemberly Lyceum Museum of Art<br>(381 Wrenfield St)</p>
    </div>
  </section>
</main>
</body>
</html>
```